New eyelid plastic surgery office needs a business card design-Eyelid Surgery Partners of Brennor

I recently used SketchHarbor for my logo design and was very pleased with creativity and results. It was a difficult decision for me. Now I would like to create a business card based on this logo, which I will attach.

The text should be easily legible as some of my patients have difficulty seeing, but I would like a subtle, sophisticated artistry also evident to make the card memorable. Would like the card based on a similar color scheme as the logo but the inverse or other complementary colors may prove interesting

A good question was asked...my concern about my visually impaired patients was really my desire to avoid italicized or calligraphic type fonts that may be hard to read. Standard font size for a business card would be fine. Thanks!

Thank you so much for the great work so far. I wanted to give you my particular contact information to see if that would change the look of the cards. Martin Pellowby, MD Address: 2817 Larkmoor Avenue, Suite 205 Wilmington, NC 28517 Phone: 910-555-0183 Fax: 910-555-0184 Website: www.brennorlidclinic.example Please delete the email slot from the card. Thanks so much!

Reason: Last minute consideration. So many great revisions right now!

Plastic

```html
<!DOCTYPE html>
<html lang="en">
<head>
<meta charset="utf-8">
<title>Eyelid Surgery Partners of Brennor – Business Card</title>
<link href="https://fonts.googleapis.com/css2?family=Questrial&display=swap" rel="stylesheet">
<style>
  :root {
    --page-bg: #e4e2de;
    --card-white: #f3f3f4;
    --card-black: #0b0b0c;
    --brand-blue: #2f4c9c;
    --brand-blue-light: #9fb0e6;
    --wave-grey: #c9c9cc;
    --ink: #2a2a2c;
  }
  * { box-sizing: border-box; margin: 0; padding: 0; }
  html, body { width: 1200px; height: 900px; overflow: hidden; }
  body {
    background: var(--page-bg);
    font-family: "Questrial", "Century Gothic", sans-serif;
    position: relative;
  }
  .card {
    position: absolute;
    left: 280px;
    width: 640px;
    height: 366px;
    border-radius: 4px;
    overflow: hidden;
    box-shadow: 0 10px 24px rgba(0,0,0,.18);
  }
  .card-back { top: 60px; background: var(--card-black); }
  .card-front { top: 470px; background: var(--card-white); }

  .brand-name {
    color: var(--brand-blue);
    text-transform: uppercase;
    line-height: 1;
  }
  .brand-name .line-main { display: block; font-size: 30px; letter-spacing: 1px; }
  .brand-name .line-sub { display: block; font-size: 17px; letter-spacing: 1px; margin-top: 6px; }

  .card-back .brand-name {
    position: absolute;
    left: 0; right: 0; top: 150px;
    text-align: center;
  }

  .card-front .brand-name {
    position: absolute;
    right: 34px; top: 34px;
    text-align: right;
  }
  .card-front .brand-name .line-main { font-size: 27px; }
  .card-front .brand-name .line-sub { font-size: 15px; }

  .holder {
    position: absolute;
    left: 40px; top: 118px;
  }
  .holder-name {
    font-size: 17px;
    letter-spacing: 2px;
    color: var(--ink);
    font-weight: 700;
  }
  .holder-title {
    font-size: 11px;
    letter-spacing: 1.5px;
    color: var(--brand-blue);
    margin-top: 6px;
  }

  .contact-list {
    position: absolute;
    left: 290px; top: 158px;
    list-style: none;
    font-size: 13px;
    letter-spacing: 2px;
    color: var(--ink);
  }
  .contact-list li {
    display: flex; align-items: center;
    height: 26px;
  }
  .contact-list .icon {
    width: 14px; height: 14px;
    margin-right: 14px;
    flex: none;
  }
  .contact-list .no-icon { margin-left: 28px; }

  .wave { position: absolute; left: 0; bottom: 0; width: 640px; height: 366px; }
</style>
</head>
<body>

  <section class="card card-back" aria-label="Business card back">
    <p class="brand-name">
      <span class="line-main">Eyelid Surgery Partners</span>
      <span class="line-sub">of Brennor</span>
    </p>
  </section>

  <section class="card card-front" aria-label="Business card front">
    <svg class="wave" viewBox="0 0 640 366" aria-hidden="true">
      <path d="M0 120 C120 170 200 290 330 330 C420 356 540 350 640 340 L640 366 L0 366 Z" fill="var(--wave-grey)"/>
      <path d="M0 135 C110 185 190 300 320 340 C420 362 540 360 640 352 L640 366 L0 366 Z" fill="var(--brand-blue-light)"/>
      <path d="M0 142 C105 195 180 305 310 345 C400 366 520 366 640 362 L640 366 L0 366 Z" fill="var(--brand-blue)"/>
    </svg>

    <p class="brand-name">
      <span class="line-main">Eyelid Surgery Partners</span>
      <span class="line-sub">of Brennor</span>
    </p>

    <div class="holder">
      <p class="holder-name">Delia Marsh Corwin</p>
      <p class="holder-title">Director of Operations</p>
    </div>

    <ul class="contact-list">
      <li><span class="no-icon">Brennor Falls | Larkmoor</span></li>
      <li>
        <svg class="icon" viewBox="0 0 16 16" aria-hidden="true"><path d="M4 1 L6.5 4.5 L5 6 C6 8.5 7.5 10 10 11 L11.5 9.5 L15 12 L13 15 C6.5 14 2 9.5 1 3 Z" fill="var(--brand-blue)"/></svg>
        301-555-0147
      </li>
      <li>
        <svg class="icon" viewBox="0 0 16 16" aria-hidden="true"><rect x="1" y="3" width="14" height="10" fill="none" stroke="var(--brand-blue)" stroke-width="1.6"/><path d="M1 3 L8 9 L15 3" fill="none" stroke="var(--brand-blue)" stroke-width="1.6"/></svg>
        dcorwin@brennorlid.example
      </li>
      <li>
        <svg class="icon" viewBox="0 0 16 16" aria-hidden="true"><circle cx="8" cy="8" r="6.5" fill="none" stroke="var(--brand-blue)" stroke-width="1.5"/><ellipse cx="8" cy="8" rx="3" ry="6.5" fill="none" stroke="var(--brand-blue)" stroke-width="1.2"/><path d="M1.5 8 H14.5" stroke="var(--brand-blue)" stroke-width="1.2"/></svg>
        www.brennorlid.example
      </li>
    </ul>
  </section>

</body>
</html>
```